Meridian Clearsound Wellness LLC Card Design

Need business card with a logo for a hearing aid sales and audiology business. We have two Hearing Instrument Specialists and one Audiologist on staff. Over 25 years in business. Locally owned and operated. Financing available. Most insurances accepted.

Meridian Clearsound Wellness LLC
48730 W Larkfield, Suite 9
Spokane, WA 99371
509-617-2084
www.meridianclearsound-example.com

Manager
Tobias Wrenfield HIS COHC
License #81957260

Target Market(s)

50yr old + people with a hearing loss.

Industry/Entity Type

Business

Contact Information for Business Card

48730 W Larkfield, Suite 9
Spokane, WA 99371
509-617-2084
www.meridianclearsound-example.com

Manager
Tobias Wrenfield HIS COHC
RTEQ #81957260

Font styles to use
Serif
Sans Serif

Requirements
Must have
• Business name, Tobias's name and title(s) and contact information, License #, web address
Nice to have
Should not have

```html
<!DOCTYPE html>
<html lang="en">
<head>
<meta charset="utf-8">
<title>Meridian Clearsound Wellness LLC – Business Card</title>
<link href="https://fonts.googleapis.com/css2?family=Exo+2:wght@500&family=Open+Sans:wght@400;600;700&display=swap" rel="stylesheet">
<style>
  :root {
    --page-bg: #e9e6e3;
    --card-white: #ffffff;
    --blue-light: #0a8fd0;
    --blue-mid: #0a5ed8;
    --blue-deep: #0019c4;
    --name-blue: #1a4fc4;
    --ink: #1a1a1a;
  }
  * { margin: 0; padding: 0; box-sizing: border-box; }
  html, body { width: 1200px; height: 900px; overflow: hidden; }
  body {
    background: var(--page-bg);
    position: relative;
    font-family: "Open Sans", Arial, sans-serif;
  }
  .card {
    position: absolute;
    border-radius: 16px;
    overflow: hidden;
    box-shadow: 0 6px 18px rgba(0,0,0,0.18);
  }

  /* Front */
  .card-front {
    left: 77px; top: 33px; width: 590px; height: 365px;
    background: var(--card-white);
  }
  .front-header {
    position: absolute; top: 28px; left: 0; width: 100%; z-index: 2;
    text-align: center; font-size: 16px; color: var(--ink);
  }
  .front-header .person { color: var(--name-blue); font-weight: 600; font-size: 17px; }
  .front-header .credentials { font-size: 14px; }
  .front-band {
    position: absolute; top: 77px; left: 0; width: 100%; height: 100px;
    background: linear-gradient(to bottom, var(--blue-light), var(--blue-deep));
  }
  .front-mark {
    position: absolute; left: 218px; top: 56px; width: 158px; height: 146px;
    border-radius: 50%; background: var(--card-white); z-index: 1;
  }
  .front-company {
    position: absolute; top: 200px; left: 0; width: 100%; z-index: 2;
    text-align: center; font-family: "Exo 2", Arial, sans-serif; font-weight: 500;
    color: var(--name-blue); line-height: 1.1;
  }
  .front-company .line-main { display: block; font-size: 30px; letter-spacing: 1px; }
  .front-company .line-sub { display: block; font-size: 16px; letter-spacing: 3px; margin-top: 4px; }
  .front-contact {
    position: absolute; top: 283px; left: 0; width: 100%;
    text-align: center; font-size: 15.5px; color: var(--ink); line-height: 34px;
  }

  /* Back */
  .card-back {
    left: 389px; top: 505px; width: 566px; height: 350px;
    background: linear-gradient(to bottom, var(--blue-mid), var(--blue-deep));
  }
  .back-top {
    position: absolute; top: 0; left: 0; width: 100%; height: 80px;
    background: linear-gradient(to bottom, var(--blue-light), #0a74c8);
  }
  .back-stripe {
    position: absolute; top: 80px; left: 0; width: 100%; height: 98px;
    background: var(--card-white);
  }
  .back-mark {
    position: absolute; left: 213px; top: 55px; width: 144px; height: 138px;
    border-radius: 50%; background: #0a6ad4;
  }
  .back-company {
    position: absolute; top: 196px; left: 0; width: 100%;
    text-align: center; font-family: "Exo 2", Arial, sans-serif; font-weight: 500;
    color: var(--card-white); line-height: 1.1;
  }
  .back-company .line-main { display: block; font-size: 28px; letter-spacing: 1px; }
  .back-company .line-sub { display: block; font-size: 15px; letter-spacing: 3px; margin-top: 3px; }
  .back-license {
    position: absolute; top: 276px; left: 0; width: 100%;
    text-align: center; color: var(--card-white); font-weight: 700; font-size: 14.5px;
  }
</style>
</head>
<body>
  <section class="card card-front" aria-label="Business card front">
    <div class="front-band"></div>
    <div class="front-mark"></div>
    <p class="front-header"><span class="person">Tobias Wrenfield</span> <span class="person credentials">HIS COHC</span> &nbsp;|&nbsp; Manager</p>
    <h1 class="front-company">
      <span class="line-main">MERIDIAN CLEARSOUND</span>
      <span class="line-sub">WELLNESS LLC</span>
    </h1>
    <div class="front-contact">
      <p>509-617-2084 &nbsp;| www.meridianclearsound-example.com</p>
      <p>48730 W Larkfield,&nbsp; Suite 9 Spokane, WA 99371</p>
    </div>
  </section>

  <section class="card card-back" aria-label="Business card back">
    <div class="back-top"></div>
    <div class="back-stripe"></div>
    <div class="back-mark"></div>
    <h2 class="back-company">
      <span class="line-main">MERIDIAN CLEARSOUND</span>
      <span class="line-sub">WELLNESS LLC</span>
    </h2>
    <p class="back-license">License #81957260</p>
  </section>
</body>
</html>
```